Relocation/furniture installation company needs new business cards

we are a relocation and furniture installation company mainly dealing with corporate clients and we are looking for new business card ideas. Cards should incorporate our logo and list our website, phone number and services. The company is only 2 years old but with more staff joining we are in the need for more business cards, so something with an awesome design that is eye catching would go a long way to insure we get our name out there and look good to potential new clients.

Target Market(s)

Corporate

Industry/Entity Type

Trade

Contact Information for Business Card

www.mervoline.co.nz
0508 4 bravok

furniture installation
business relocations
joinery installation
commercial property maintenance

Colors
0592cd
34a7d8
85cae6
85acd3
0356a4
cfdfed
cee9f5
757575
474747

Requirements
Must have
• Business relocations and furniture installation specialists
Nice to have
• something that incorporates our logo.

```html
<!DOCTYPE html>
<html lang="en">
<head>
<meta charset="utf-8">
<title>Mervoline Business Cards</title>
<link href="https://fonts.googleapis.com/css2?family=Michroma&family=Roboto:wght@400;700&display=swap" rel="stylesheet">
<style>
  :root {
    --backdrop: #2a2a2a;
    --card-white: #f2f2f2;
    --card-blue: #00b2f6;
    --brand-navy: #2e3192;
    --brand-mark: #2e3192;
    --accent-cyan: #00aeef;
    --text-grey: #474747;
    --text-white: #ffffff;
  }
  * { margin: 0; padding: 0; box-sizing: border-box; }
  html, body { width: 1200px; height: 960px; overflow: hidden; }
  body { background: var(--backdrop); position: relative; font-family: "Roboto", Arial, sans-serif; }
  .card {
    position: absolute;
    width: 600px;
    height: 343px;
    box-shadow: 0 3px 6px rgba(0,0,0,0.5);
    text-align: center;
  }
  .card-front { left: 314px; top: 113px; background: var(--card-white); }
  .card-back { left: 311px; top: 472px; background: var(--card-blue); }
  .brand-square {
    position: absolute;
    left: 50%;
    background: var(--brand-mark);
  }
  .card-front .brand-square { top: 72px; width: 72px; height: 72px; margin-left: -36px; }
  .card-back .brand-square { top: 122px; width: 64px; height: 64px; margin-left: -32px; }
  .brand-name {
    position: absolute;
    left: 0; right: 0;
    font-family: "Michroma", "Arial Black", sans-serif;
    color: var(--brand-navy);
    font-weight: 400;
    letter-spacing: 2px;
    line-height: 1;
  }
  .card-front .brand-name { top: 154px; font-size: 33px; }
  .card-back .brand-name { top: 199px; font-size: 30px; }
  .person-name {
    position: absolute; left: 0; right: 0; top: 219px;
    font-family: "Michroma", Arial, sans-serif;
    font-size: 16px; letter-spacing: 2px;
    color: var(--brand-navy);
  }
  .person-role {
    position: absolute; left: 0; right: 0; top: 240px;
    font-family: "Michroma", Arial, sans-serif;
    font-size: 11px; letter-spacing: 1.5px;
    color: var(--accent-cyan);
  }
  .contact-line {
    position: absolute; left: 0; right: 0; top: 261px;
    font-size: 14.5px; color: var(--text-grey);
  }
  .contact-label { font-weight: 700; color: var(--brand-navy); }
  .service-list {
    position: absolute; left: 0; right: 0; top: 276px;
    font-size: 15px; line-height: 18px; color: var(--text-white);
    list-style: none;
  }
</style>
</head>
<body>
  <section class="card card-front">
    <div class="brand-square" aria-hidden="true"></div>
    <div class="brand-name">MERVOLINE</div>
    <div class="person-name">AARON PELL</div>
    <div class="person-role">CEO/Founder</div>
    <p class="contact-line"><span class="contact-label">P.</span> 0508 4 bravok <span class="contact-label">W.</span> www.mervoline.co.nz</p>
  </section>

  <section class="card card-back">
    <div class="brand-square" aria-hidden="true"></div>
    <div class="brand-name">MERVOLINE</div>
    <ul class="service-list">
      <li>Furniture installation | Business relocations</li>
      <li>Joinery installation | Commercial Property maintenance</li>
    </ul>
  </section>
</body>
</html>
```